Postcard Design

Postcard for the following:

Front of postcard:
A new little beauty and health haven has opened up just around the corner at 42 Marston Lane, Fernwood Rise.
Just like you, Mabel’s Lantern is special, offering treatments and services tailor made to your specific needs. Mabel has over 24 years of industry experience and offers a unique approach to helping you feel healthful, nourished and happy. Her treatments are brilliantly effective and include remedial massage therapies and reflexology, gorgeous rejuvenating facials and much much more…………..come and experience this unique and 100% organic little piece of heaven.
You deserve to feel great so we work from the inside out by offering nutritional health advice and formulations developed especially for you. We wholly nourish the individual in the wise woman tradition of healing and happiness.
As a special welcome gift I would like to offer you $15 off any service
By appointment 027 5162930 I look forward to seeing you soon

Back of postcard:
The hearth has been the centre of human life for at least 400,000 years. it is the place where people meet to cook, eat, talk together and heal. The ' hearth' was the heart of the home It was the centre of activity, where everyone gathered to keep warm, laugh, listen to the stories of old and heal. It was the place of physical and emotional nourishment. The hearth is a symbol for the hospitality and living spirit of the home.

Industry/Entity Type

Hospitality

Requirements
Nice to have
• A logo for the business would be really good.

```html
<!DOCTYPE html>
<html lang="en">
<head>
<meta charset="utf-8">
<title>Mabel’s Lantern – Postcard</title>
<link rel="stylesheet" href="https://fonts.googleapis.com/css2?family=Open+Sans:ital,wght@0,400;0,700;1,700&family=Arimo&display=swap">
<style>
  :root {
    --navy: #1d1174;
    --navy-deep: #150c5c;
    --violet: #7b4fc8;
    --violet-light: #a27be0;
    --white: #ffffff;
    --zone-pink: #fdeef6;
    --zone-yellow: #fefee6;
    --frame-pink: #f3c6cf;
    --frame-cyan: #cdf1f4;
    --label-grey: #b9b9bf;
    --skin-light: #f1d3c0;
    --skin-mid: #d7a68a;
    --hair: #5a3a22;
  }
  html, body { margin: 0; padding: 0; overflow: hidden; background: var(--white); }
  .canvas { position: relative; width: 764px; height: 1200px; overflow: hidden; background: var(--white); font-family: "Open Sans", Verdana, sans-serif; }

  /* Front */
  .front-photo {
    position: absolute; left: 0; top: 0; width: 764px; height: 338px;
    background: linear-gradient(100deg, var(--hair) 0%, var(--skin-mid) 18%, var(--skin-light) 40%, #f6e3d6 60%, var(--skin-mid) 80%, #e9d5cf 100%);
  }
  .brand-panel {
    position: absolute; right: 0; top: 0; width: 221px; height: 190px;
    background: linear-gradient(180deg, var(--violet) 0%, var(--violet-light) 70%, rgba(162,123,224,0) 100%);
  }
  .brand-name {
    position: absolute; left: 0; right: 0; top: 40px; text-align: center;
    font-weight: 700; font-size: 44px; color: var(--white); letter-spacing: 0.5px;
  }
  .front-message {
    position: absolute; left: 0; top: 338px; width: 764px; height: 254px;
    background: var(--navy); box-sizing: border-box; padding: 16px 33px 0 30px;
    color: var(--white); font-weight: 700; font-size: 12.6px; line-height: 16px;
    text-align: justify; text-shadow: 1px 1px 1px #000;
  }
  .front-message p { margin: 0 0 8px; text-indent: 21px; }

  /* Back */
  .frame-outer { position: absolute; left: 8px; top: 614px; width: 746px; height: 577px; border: 4px solid var(--frame-pink); }
  .frame-inner { position: absolute; left: 15px; top: 621px; width: 730px; height: 562px; border: 4px solid var(--frame-cyan); background: var(--zone-pink); }
  .zone-scan { position: absolute; left: 22px; top: 797px; width: 348px; height: 381px; background: var(--zone-yellow); }
  .zone-address { position: absolute; left: 370px; top: 797px; width: 375px; height: 298px; background: var(--zone-pink); }
  .zone-barcode { position: absolute; left: 96px; top: 1095px; width: 649px; height: 83px; background: var(--zone-pink); }
  .zone-label { position: absolute; font-family: "Arimo", Arial, sans-serif; color: var(--label-grey); }
  .label-title { font-size: 21px; text-align: center; line-height: 27px; }
  .label-note { font-size: 14.5px; line-height: 19px; }

  .story-panel {
    position: absolute; left: 0; top: 608px; width: 575px; height: 189px;
    background: var(--navy); box-sizing: border-box; padding: 48px 22px 0 32px;
    color: var(--white); font-weight: 700; font-style: italic; font-size: 12.4px; line-height: 15.6px;
    text-shadow: 1px 1px 1px #000;
  }
  .story-panel p { margin: 0; }
</style>
</head>
<body>
<div class="canvas">
  <section class="postcard-front">
    <div class="front-photo" role="img" aria-label="Photo of a woman relaxing during a facial massage, with frangipani flowers in the corner"></div>
    <div class="brand-panel">
      <div class="brand-name">Mabel</div>
    </div>
    <div class="front-message">
      <p>A new little beauty and health haven has opened up just around the corner at 42 Marston Lane, Fernwood Rise.</p>
      <p>Just like you, Mabel’s Lantern is special, offering treatments and services tailor made to your specific needs. Mabel has over 24 years of industry experience and offers a unique approach to helping you feel healthful, nourished and happy. Her treatments are brilliantly effective and include remedial massage therapies and reflexology, gorgeous rejuvenating facials and much much more… come and experience this unique and 100% organic little piece of heaven.</p>
      <p>You deserve to feel great so we work from the inside out by offering nutritional health advice and formulations developed especially for you. We wholly nourish the individual in the wise woman tradition of healing and happiness.</p>
      <p>As a special welcome gift I would like to offer you $15 off any service.</p>
      <p>By appointment 027 5162930. I look forward to seeing you soon.</p>
    </div>
  </section>

  <section class="postcard-back">
    <div class="frame-outer"></div>
    <div class="frame-inner"></div>
    <div class="zone-scan"></div>
    <div class="zone-address"></div>
    <div class="zone-barcode"></div>

    <div class="zone-label label-title" style="left:575px; top:684px; width:170px;">Postage<br>Area</div>
    <div class="zone-label label-title" style="left:370px; top:841px; width:380px;">Address Area</div>
    <div class="zone-label label-title" style="left:96px; top:1128px; width:665px;">Barcode Area</div>
    <div class="zone-label label-note" style="left:50px; top:906px; width:300px;">This zone should contain no addresses that include a zip code or state. The Post Office will scan this entire area for recipient addresses and zip codes.</div>
    <div class="zone-label label-note" style="left:409px; top:906px; width:320px;">The only text allowed in the Address Area is the recipient mailing address.<br>Red zones may have no text or graphics darker than 7% grayscale.</div>

    <div class="story-panel">
      <p>The hearth has been the centre of human life for at least 400,000 years. it is the place where people meet to cook, eat, talk together and heal. The ' hearth' was the heart of the home It was the centre of activity, where everyone gathered to keep warm, laugh, listen to the stories of old and heal. It was the place of physical and emotional nourishment. The hearth is a symbol for the hospitality and living spirit of the home.</p>
    </div>
  </section>
</div>
</body>
</html>
```